Mondaxe custom business card design

Need a authentic, innovative business card design for a new mobile app business. I am uploading a few screen images from our app for you to view. I would like app design theme to match business card design. I can also send logo images.

```html
<!DOCTYPE html>
<html lang="en">
<head>
<meta charset="utf-8">
<title>Mondaxe Business Card</title>
<link href="https://fonts.googleapis.com/css2?family=Roboto:wght@400;500;700;900&display=swap" rel="stylesheet">
<style>
  :root {
    --page-bg: #d9d9db;
    --card-dark: #000000;
    --card-light: #ffffff;
    --brand-purple: #6a2aa0;
    --text-dark: #1c1c1c;
    --text-muted: #555555;
    --divider: #b8b8b8;
  }
  * { margin: 0; padding: 0; box-sizing: border-box; }
  html, body {
    width: 1200px; height: 874px; overflow: hidden;
    background: var(--page-bg);
    font-family: "Roboto", sans-serif;
  }
  .canvas {
    position: relative; width: 1200px; height: 874px;
  }
  .card {
    position: absolute; left: 240px; width: 720px; height: 411px;
    box-shadow: 0 6px 18px rgba(0,0,0,0.25);
  }
  .card-front { top: 20px; background: var(--card-dark); }
  .card-back { top: 443px; background: var(--card-light); }

  .brand {
    position: absolute; left: 0; right: 0; top: 150px;
    display: flex; flex-direction: column; align-items: center; gap: 22px;
  }
  .brand-dot {
    width: 64px; height: 64px; border-radius: 50%;
    background: var(--brand-purple);
  }
  .brand-name {
    font-weight: 900; font-size: 56px; color: var(--card-light);
    letter-spacing: 0.5px;
  }

  .identity {
    position: absolute; right: 396px; top: 120px; text-align: right;
  }
  .person-name {
    font-weight: 500; font-size: 27px; color: var(--brand-purple);
    letter-spacing: -0.3px;
  }
  .person-role {
    font-weight: 400; font-size: 18px; color: var(--text-dark); margin-top: 2px;
  }
  .divider {
    position: absolute; left: 356px; top: 105px; width: 2px; height: 130px;
    background: linear-gradient(to bottom, transparent, var(--divider) 25%, var(--divider) 75%, transparent);
  }
  .contacts {
    position: absolute; left: 378px; top: 112px; list-style: none;
  }
  .contacts li {
    display: flex; align-items: center; gap: 12px;
    font-size: 18px; color: var(--text-muted); line-height: 23px;
  }
  .contacts svg { width: 15px; height: 15px; fill: var(--brand-purple); flex: none; }
  .address {
    position: absolute; left: 110px; bottom: 70px;
    display: flex; align-items: center; gap: 10px;
    font-size: 19px; color: var(--text-muted);
  }
  .address svg { width: 15px; height: 20px; fill: var(--brand-purple); }
</style>
</head>
<body>
<main class="canvas">
  <section class="card card-front">
    <div class="brand">
      <span class="brand-dot"></span>
      <span class="brand-name">Mondaxe</span>
    </div>
  </section>

  <section class="card card-back">
    <div class="identity">
      <p class="person-name">ELENA MARSH</p>
      <p class="person-role">CEO/FOUNDER</p>
    </div>
    <div class="divider"></div>
    <ul class="contacts">
      <li><svg viewBox="0 0 24 24"><path d="M6.6 10.8a15 15 0 0 0 6.6 6.6l2.2-2.2a1 1 0 0 1 1-.25 11.4 11.4 0 0 0 3.6.57 1 1 0 0 1 1 1V20a1 1 0 0 1-1 1A17 17 0 0 1 3 4a1 1 0 0 1 1-1h3.5a1 1 0 0 1 1 1c0 1.25.2 2.45.57 3.57a1 1 0 0 1-.25 1z"/></svg>555 214 7730</li>
      <li><svg viewBox="0 0 24 24"><path d="M7 1h10a2 2 0 0 1 2 2v18a2 2 0 0 1-2 2H7a2 2 0 0 1-2-2V3a2 2 0 0 1 2-2zm0 3v14h10V4z"/></svg>555 382 6159</li>
      <li><svg viewBox="0 0 24 24"><path d="M6 2h9l3 3v4H6zM4 10h16a2 2 0 0 1 2 2v8H2v-8a2 2 0 0 1 2-2zm2 4v2h4v-2z"/></svg>555 907 4418</li>
      <li><svg viewBox="0 0 24 24"><path d="M2 5h20v14H2zm2 2v.5l8 5 8-5V7l-8 5z"/></svg>elena@mondaxe.com</li>
      <li><svg viewBox="0 0 24 24"><circle cx="12" cy="12" r="10"/></svg>www.mondaxe.com</li>
    </ul>
    <p class="address">
      <svg viewBox="0 0 24 32"><path d="M12 0a12 12 0 0 0-12 12c0 9 12 20 12 20s12-11 12-20A12 12 0 0 0 12 0zm0 17a5 5 0 1 1 0-10 5 5 0 0 1 0 10z"/></svg>
      4120 Larkspur Court, Juneau, Alaska 99801
    </p>
  </section>
</main>
</body>
</html>
```